Business Card Design for Kidvale (Hires out childrens play areas)

Looking to have a business card designed for a company we just bought. The company rents out childrens play areas.

I have uploaded a couple of examples of the kind of business card style I like. Here are two more examples:

https://quorvastudio.nz/project/bright-romp-branding/
https://imgvaultcdn.com/design_img/8841052/302917/302917_5518203_8841052_b73e19a2_image.jpg

I think a white card will be best due to all the colours in the logo.

Size we require: 3.75" x 2.25" (horizontally orientated) with a 0.125" bleed

Uploaded is two versions of our logo.

Details for the card:
1. My name: Liam Verster
2. Title: Managing Director
3. Phone no: 021 563 417
4. Email: liam@kidvale.co.nz
5. URL: www.kidvale.co.nz
6. Address:
PO Box 318625
Fernlea, Auckland

Let me know if you need anything else.

Target Market(s)

Hospitals, doctors surgeries, bed shops, etc.

Contact Information for Business Card

Details for the card:
1. My name: Liam Verster
3. Phone no: 021 563 417
5. URL: www.kidvale.co.nz
6. Address:
PO Box 318625
Fernlea, Auckland

Requirements
Should not have
• Not too busy.

```html
<!DOCTYPE html>
<html lang="en">
<head>
<meta charset="utf-8">
<title>Kidvale Business Card</title>
<link href="https://fonts.googleapis.com/css2?family=Montserrat:wght@500;600;700;800&display=swap" rel="stylesheet">
<style>
  :root {
    --page: #e6e8ec;
    --blue: #1466b8;
    --blue-light: #2a9be0;
    --blue-deep: #0b5aa8;
    --ink: #2b2b2b;
    --white: #ffffff;
    --purple: #8a2f9c;
    --magenta: #d2198a;
    --card-shadow: 0 14px 30px rgba(0,0,0,0.22);
  }
  * { box-sizing: border-box; margin: 0; padding: 0; }
  html, body {
    width: 1200px; height: 900px; overflow: hidden;
    background: var(--page);
    font-family: "Montserrat", sans-serif;
  }
  .canvas { position: relative; width: 1200px; height: 900px; }

  .card {
    position: absolute;
    width: 660px; height: 396px;
    border-radius: 26px;
    overflow: hidden;
    box-shadow: var(--card-shadow);
  }

  /* Front */
  .card-front {
    left: 200px; top: 50px;
    background: radial-gradient(ellipse at 50% 40%, var(--blue-light) 0%, var(--blue) 55%, var(--blue-deep) 100%);
    display: flex; align-items: center; justify-content: center;
  }
  .brand {
    display: flex; align-items: center; gap: 18px;
    color: var(--white);
    font-weight: 800;
    font-size: 64px;
    letter-spacing: 1px;
  }
  .brand-dot {
    width: 44px; height: 44px; border-radius: 50%;
    background: var(--white);
  }

  /* Back */
  .card-back {
    left: 340px; top: 474px;
    background: var(--white);
  }
  .mascot-area {
    position: absolute;
    right: -120px; top: -70px;
    width: 500px; height: 520px;
    border-radius: 50%;
    background: linear-gradient(160deg, var(--purple) 0%, var(--magenta) 100%);
    opacity: 0.9;
  }
  .details {
    position: absolute; left: 44px; top: 58px;
    color: var(--ink);
  }
  .name {
    color: var(--blue);
    font-weight: 800;
    font-size: 30px;
    line-height: 1;
  }
  .title {
    margin-top: 8px;
    font-weight: 600;
    font-size: 13.5px;
    letter-spacing: 1px;
    text-transform: uppercase;
  }
  .contacts { margin-top: 22px; list-style: none; }
  .contacts li {
    display: flex; align-items: center; gap: 9px;
    font-weight: 500; font-size: 16px; line-height: 22px;
  }
  .contacts svg { width: 15px; height: 15px; fill: var(--blue); flex: none; }
  .small-brand {
    margin-top: 26px;
    display: flex; align-items: center; gap: 10px;
    color: var(--blue);
    font-weight: 800; font-size: 30px;
  }
  .small-brand .brand-dot { width: 22px; height: 22px; background: var(--blue); }
  .address {
    margin-top: 14px;
    font-weight: 600; font-size: 17px; line-height: 22px;
    font-style: normal;
  }
</style>
</head>
<body>
<main class="canvas">
  <section class="card card-front" aria-label="Card front">
    <div class="brand"><span class="brand-dot"></span>Kidvale</div>
  </section>

  <section class="card card-back" aria-label="Card back">
    <div class="mascot-area" role="img" aria-label="Large brand mascot decoration in purple and magenta"></div>
    <div class="details">
      <h1 class="name">Liam<br>Verster</h1>
      <p class="title">Managing Director</p>
      <ul class="contacts">
        <li><svg viewBox="0 0 16 16"><path d="M3.5 1.5l2.5 2.8-1.5 1.8c.9 2 2.4 3.5 4.4 4.4l1.8-1.5 2.8 2.5-1.6 2C7 13 3 9 1.5 3.1z"/></svg>021 563 417</li>
        <li><svg viewBox="0 0 16 16"><path d="M1 3h14v10H1z M1.5 3.5L8 9l6.5-5.5" stroke="#fff" stroke-width="1.2"/></svg>liam@kidvale.co.nz</li>
        <li><svg viewBox="0 0 16 16"><circle cx="8" cy="8" r="7"/><path d="M1 8h14M8 1c-3 3.5-3 10.5 0 14M8 1c3 3.5 3 10.5 0 14" stroke="#fff" stroke-width="1" fill="none"/></svg>www.kidvale.co.nz</li>
      </ul>
      <div class="small-brand"><span class="brand-dot"></span>Kidvale</div>
      <address class="address">PO Box 318625<br>Fernlea, Auckland</address>
    </div>
  </section>
</main>
</body>
</html>
```